Solar energy proposal for homeowners

I am providing households with solar energy proposals, and I need a high-quality brochure that is packaged cleverly to attract the homeowner's attention. Take a look at the one page solar brochure that I have included to get an idea of text and content.

Target Market(s)

Residential Homeowners

Industry/Entity Type

Solar

Requirements
Must have
• High quality document

```html
<!DOCTYPE html>
<html lang="en">
<head>
<meta charset="utf-8">
<title>Brightvale Energy – Presentation Folder</title>
<link href="https://fonts.googleapis.com/css2?family=Montserrat:wght@300;400;600;700&family=Open+Sans:wght@400;600&display=swap" rel="stylesheet">
<style>
  :root {
    --backdrop: #e4e4e6;
    --ocean-light: #0eaccd;
    --ocean-deep: #067f9e;
    --teal: #26b0a6;
    --leaf: #66b972;
    --leaf-deep: #579a5f;
    --paper: #f4f4f4;
    --paper-shade: #dcdcdc;
    --ink: #4a4a4a;
    --white: #ffffff;
  }
  * { box-sizing: border-box; margin: 0; padding: 0; }
  html, body { width: 1200px; height: 853px; overflow: hidden; }
  body {
    background: var(--backdrop);
    font-family: "Open Sans", Arial, sans-serif;
    display: flex; align-items: center; justify-content: center;
  }
  .folder-spread { display: flex; width: 1080px; height: 720px; box-shadow: 0 10px 30px rgba(0,0,0,.18); }
  .panel { position: relative; width: 540px; height: 720px; overflow: hidden; }
  .panel svg.panel-art { position: absolute; inset: 0; }

  /* back cover */
  .back-brand {
    position: absolute; left: 0; right: 0; top: 498px;
    display: flex; align-items: center; justify-content: center; gap: 12px;
  }
  .brand-square { width: 30px; height: 30px; background: var(--ocean-light); flex: none; }
  .brand-name {
    font-family: "Montserrat", sans-serif; font-weight: 300;
    font-size: 34px; color: var(--ocean-light); letter-spacing: .5px; white-space: nowrap;
  }
  .back-contact {
    position: absolute; left: 0; right: 0; top: 572px;
    text-align: center; font-size: 11.5px; color: var(--ink); line-height: 1.9;
  }
  .contact-line { display: flex; justify-content: center; align-items: center; gap: 14px; }
  .contact-item { display: inline-flex; align-items: center; gap: 5px; }
  .contact-item svg { width: 12px; height: 12px; }
  .social-row { display: flex; justify-content: center; gap: 6px; margin-top: 8px; }
  .social-dot { width: 18px; height: 18px; border-radius: 50%; background: var(--ocean-deep); }

  /* front cover */
  .front-brand {
    position: absolute; top: 28px; left: 0; right: 0;
    display: flex; flex-direction: column; align-items: center; gap: 6px;
  }
  .front-brand .brand-row { display: flex; align-items: center; gap: 12px; }
  .front-brand .brand-name { font-size: 36px; }
  .tagline { font-size: 11px; color: var(--white); font-weight: 600; letter-spacing: .3px; text-shadow: 0 1px 2px rgba(0,0,0,.25); }
  .front-headline {
    position: absolute; left: 0; right: 0; top: 622px;
    text-align: center; color: var(--white);
  }
  .front-headline h1 {
    font-family: "Montserrat", sans-serif; font-weight: 700; font-size: 24px; letter-spacing: .3px;
  }
  .front-headline p {
    font-family: "Montserrat", sans-serif; font-weight: 600; font-size: 13px; margin-top: 8px;
  }
</style>
</head>
<body>
<main class="folder-spread">

  <section class="panel back-cover">
    <svg class="panel-art" viewBox="0 0 540 720" width="540" height="720">
      <defs>
        <linearGradient id="oceanBack" x1="0" y1="0" x2="1" y2="0">
          <stop offset="0" stop-color="var(--ocean-deep)" stop-opacity=".9"/>
          <stop offset=".6" stop-color="var(--ocean-light)"/>
          <stop offset="1" stop-color="var(--ocean-deep)"/>
        </linearGradient>
        <linearGradient id="paperBack" x1="0" y1="0" x2="1" y2="1">
          <stop offset="0" stop-color="var(--paper-shade)"/>
          <stop offset=".5" stop-color="var(--paper)"/>
          <stop offset="1" stop-color="var(--paper-shade)"/>
        </linearGradient>
      </defs>
      <rect width="540" height="720" fill="url(#paperBack)"/>
      <path d="M0,0 H540 V400 Q270,410 0,418 Z" fill="url(#oceanBack)"/>
      <path d="M0,418 Q270,410 540,400" fill="none" stroke="var(--white)" stroke-width="4"/>
      <polygon points="0,430 270,428 0,600" fill="var(--leaf-deep)"/>
    </svg>

    <div class="back-brand">
      <span class="brand-square"></span>
      <span class="brand-name">Brightvale Energy</span>
    </div>

    <div class="back-contact">
      <div>Brightvale Energy, LLC 1420 Harbor Pine Road Tampa, FL 33602</div>
      <div class="contact-line">
        <span class="contact-item">
          <svg viewBox="0 0 24 24"><path d="M6.6 10.8a15 15 0 0 0 6.6 6.6l2.2-2.2a1 1 0 0 1 1-.25 11 11 0 0 0 3.6.6 1 1 0 0 1 1 1V20a1 1 0 0 1-1 1A17 17 0 0 1 3 4a1 1 0 0 1 1-1h3.5a1 1 0 0 1 1 1 11 11 0 0 0 .6 3.6 1 1 0 0 1-.25 1z" fill="var(--teal)"/></svg>
          555.014.2290
        </span>
        <span class="contact-item">
          <svg viewBox="0 0 24 24"><rect x="3" y="5" width="18" height="14" rx="2" fill="none" stroke="var(--teal)" stroke-width="2"/><path d="M3 7l9 6 9-6" fill="none" stroke="var(--teal)" stroke-width="2"/></svg>
          hello@brightvaleenergy.com
        </span>
        <span class="contact-item">
          <svg viewBox="0 0 24 24"><circle cx="12" cy="12" r="9" fill="none" stroke="var(--teal)" stroke-width="2"/><path d="M3 12h18M12 3c3 3 3 15 0 18M12 3c-3 3-3 15 0 18" fill="none" stroke="var(--teal)" stroke-width="1.6"/></svg>
          www.brightvaleenergy.com
        </span>
      </div>
      <div class="social-row">
        <span class="social-dot"></span><span class="social-dot"></span><span class="social-dot"></span>
      </div>
    </div>
  </section>

  <section class="panel front-cover">
    <svg class="panel-art" viewBox="0 0 540 720" width="540" height="720">
      <defs>
        <linearGradient id="photoTone" x1="0" y1="0" x2="0.25" y2="1">
          <stop offset="0" stop-color="#7fb0e0"/>
          <stop offset=".22" stop-color="#b9d3ea"/>
          <stop offset=".38" stop-color="#5a6f9c"/>
          <stop offset=".52" stop-color="#8a5a48"/>
          <stop offset=".66" stop-color="#eef0f0"/>
          <stop offset=".82" stop-color="#9a9a90"/>
          <stop offset="1" stop-color="#6f9a3c"/>
        </linearGradient>
        <linearGradient id="tealFront" x1="0" y1="0" x2="1" y2="0">
          <stop offset="0" stop-color="var(--teal)"/>
          <stop offset="1" stop-color="var(--ocean-deep)"/>
        </linearGradient>
      </defs>
      <rect width="540" height="720" fill="var(--leaf)"/>
      <polygon points="375,468 540,405 540,520" fill="var(--leaf-deep)"/>
      <path d="M0,525 Q150,490 280,438 L540,520 V720 H0 Z" fill="url(#tealFront)"/>
      <g role="img" aria-label="Photo of a white modern house with solar panels on a tiled roof, terrace and green lawn under a blue sky">
        <polygon points="0,0 540,0 540,405 375,468 0,345" fill="url(#photoTone)"/>
      </g>
      <path d="M0,525 Q150,490 280,438" fill="none" stroke="var(--white)" stroke-width="4"/>
      <path d="M375,468 L540,520" fill="none" stroke="var(--white)" stroke-width="4"/>
      <path d="M375,468 L540,405" fill="none" stroke="var(--white)" stroke-width="4"/>
    </svg>

    <div class="front-brand">
      <div class="brand-row">
        <span class="brand-square"></span>
        <span class="brand-name">Brightvale Energy</span>
      </div>
      <span class="tagline">Rent Solar. Generate Power. Save Smarter.</span>
    </div>

    <div class="front-headline">
      <h1>Cut Your Electricity Bill By 50%</h1>
      <p>Our Mission Is To Become The Most Trusted Name In Solar</p>
    </div>
  </section>

</main>
</body>
</html>
```